Corporate Financial Services

This is a new Company. The ROW represents my son's and my own Christian name initials (ROW) (Colin and Brent) but no real significance.
This is a boutique financial services company active in the full parameter of corporate and business transactions. From standard financial and tax services to specialised Research & Development, mergers and acquisitions, business valuations, and capital raising.
Over 30 years of experience with listed and private entities.
I am after something exciting, given the nature of the business, bright, clean and colourful, but not in comic form.
Hi there,
Firstly thankyou for accepting the challenge. I have no ideas and nothing to compare your submissions with other than other peoples cards.
A few points
I omitted the ABN number from the card description. This is an important reference for all businesses operating in Australia. Therefore the following should be shown in association with the company name ROW Corporate & Financial Services Pty Ltd It can either be within brackets or without but always shown underneath the company name in smaller font.
The eight core business services need to be shown on the reverse
My contact number should also be shown along side the address
My business title is Chartered Accountant in full. I am also not fussed as to whether my name appears in caps or Caps and lowercase ie Brent Ashdown or BRENT ASHDOWN but this will depend upon the design of the rest of the card.
Maybe a small logo for the company needs to be attached but not sure.
Kind regards
Brent Ashdown
Financial
ROW Corporate & Financial Services Pty Ltd
(ABN 71 309 482 157)
(Note ABN could be shown on the reverse side with just ROW Corporate & Financial Services Pty Ltd on the front....no ABN
17 Wattlebank Street Norvale SA 5174
Brent Ashdown
Chartered Accountant
Phone (symbol preferred) +61 (0) 437 215604
Email (symbol) to be provided
www.rowfinsvc-example.com.au
Skype brent7312
- On the reverse:
Corporate Finance
Taxation
Research & Development Specialisation
Financial Accounting
Mergers & Acquisitions
Company Listings (IPO's)
Business Valuations
Capital Raising
- Interested in a strong black card (or grey white platinum and black colours) with either platinum or gold highlight modern name style no italics. I would also like at a later stage with the winner to use this same design for card for Asia with a red and or gold and platinum colour. But I want this batch first.
The smart block (square) for digital image transfer to mobile phones contained within a gold or platinum square border on reverse of the card
Anything old or staid looking. No italics sans serif

```html
<!DOCTYPE html>
<html lang="en">
<head>
<meta charset="utf-8">
<title>ROW Corporate &amp; Financial Services – Business Card</title>
<link rel="stylesheet" href="https://fonts.googleapis.com/css2?family=PT+Sans:wght@400;700&display=swap">
<style>
  :root {
    --canvas: #e4e2de;
    --card-black: #231f20;
    --card-black-soft: #2e2a2b;
    --band-white: #f4f4f4;
    --ink-dark: #3a3a3a;
    --ink-light: #ffffff;
    --ink-muted: #c9c9c9;
    --platinum: #d9dbdd;
    --shadow: rgba(0, 0, 0, 0.28);
  }
  * { box-sizing: border-box; margin: 0; padding: 0; }
  html, body {
    width: 1200px; height: 1024px; overflow: hidden;
    background: var(--canvas);
  }
  .sheet {
    width: 1200px; height: 1024px;
    display: flex; flex-direction: column;
    align-items: center; justify-content: center; gap: 30px;
  }
  .card {
    position: relative;
    width: 820px; height: 469px;
    background: var(--card-black);
    overflow: hidden;
    box-shadow: 0 10px 24px var(--shadow);
    font-family: "PT Sans", sans-serif;
  }

  /* Front */
  .card-front .stripes {
    position: absolute; inset: 0; width: 100%; height: 100%;
  }
  .card-front .sheen {
    position: absolute; inset: 0;
    background: linear-gradient(160deg, rgba(255,255,255,0.08) 0%, rgba(255,255,255,0) 45%);
  }
  .name-band {
    position: absolute; left: 330px; right: 0; top: 140px; height: 112px;
    background: var(--band-white);
    display: flex; align-items: center; gap: 22px;
    padding-left: 26px;
  }
  .brand-square {
    width: 62px; height: 62px; flex: none;
    background: var(--ink-dark);
  }
  .company-name {
    font-family: "PT Sans", sans-serif;
    font-weight: 400;
    font-size: 33px; line-height: 1.12;
    color: var(--ink-dark);
  }
  .company-name .suffix { font-size: 14px; }
  .web-line {
    position: absolute; left: 356px; top: 268px;
    display: flex; align-items: center; gap: 10px;
    font-weight: 700; font-size: 16px; color: var(--ink-light);
  }
  .web-line .globe { width: 16px; height: 16px; }

  /* Back */
  .card-back {
    background: linear-gradient(150deg, var(--card-black-soft) 0%, var(--card-black) 60%);
  }
  .services {
    position: absolute; left: 60px; top: 70px;
    list-style: none; color: var(--ink-muted);
  }
  .services li {
    font-size: 16px; line-height: 1.75;
    padding-left: 16px; position: relative;
  }
  .services li::before {
    content: ""; position: absolute; left: 0; top: 11px;
    width: 6px; height: 6px; background: var(--platinum);
  }
  .smart-square {
    position: absolute; left: 60px; top: 326px;
    width: 100px; height: 100px;
    border: 3px solid var(--platinum);
    background: var(--card-black-soft);
  }
  .contact {
    position: absolute; right: 60px; top: 70px;
    text-align: right; color: var(--ink-light);
  }
  .contact .person {
    font-weight: 700; font-size: 32px; letter-spacing: 0.5px;
  }
  .contact .title {
    font-size: 19px; color: var(--ink-muted); margin-top: 6px; margin-bottom: 34px;
  }
  .contact-list { list-style: none; }
  .contact-list li {
    display: flex; justify-content: flex-end; align-items: center; gap: 12px;
    font-size: 16px; font-weight: 700; line-height: 1.95;
  }
  .contact-list svg { width: 16px; height: 16px; flex: none; }
</style>
</head>
<body>
<main class="sheet">

  <section class="card card-front" aria-label="Business card front">
    <svg class="stripes" viewBox="0 0 820 469" preserveAspectRatio="none" aria-hidden="true">
      <polygon points="0,0 60,0 0,469" fill="#e8e8e8"/>
      <polygon points="60,0 130,0 0,469 0,469" fill="#dcdcdc"/>
      <polygon points="130,0 200,0 70,469 0,469" fill="#cfcfcf"/>
      <polygon points="200,0 270,0 140,469 70,469" fill="#bdbdbd"/>
      <polygon points="270,0 340,0 210,469 140,469" fill="#a6a6a6"/>
      <polygon points="340,0 410,0 280,469 210,469" fill="#8a8a8a"/>
      <polygon points="410,0 480,0 350,469 280,469" fill="#6a6a6a"/>
      <polygon points="480,0 550,0 420,469 350,469" fill="#474546"/>
    </svg>
    <div class="sheen"></div>

    <div class="name-band">
      <span class="brand-square"></span>
      <h1 class="company-name">ROW Corporate &amp;<br>Financial Services <span class="suffix">Pty Ltd</span></h1>
    </div>

    <p class="web-line">
      <svg class="globe" viewBox="0 0 16 16" aria-hidden="true">
        <circle cx="8" cy="8" r="7" fill="none" stroke="#fff" stroke-width="1.4"/>
        <ellipse cx="8" cy="8" rx="3" ry="7" fill="none" stroke="#fff" stroke-width="1.2"/>
        <line x1="1" y1="8" x2="15" y2="8" stroke="#fff" stroke-width="1.2"/>
      </svg>
      www.rowfinsvc-example.com.au | ABN 71 309 482 157
    </p>
  </section>

  <section class="card card-back" aria-label="Business card back">
    <ul class="services">
      <li>Corporate Finance</li>
      <li>Taxation</li>
      <li>Research &amp; Development Specialisation</li>
      <li>Financial Accounting</li>
      <li>Mergers &amp; Acquisitions</li>
      <li>Company Listings (IPO's)</li>
      <li>Business Valuations</li>
      <li>Capital Raising</li>
    </ul>
    <div class="smart-square" role="img" aria-label="Smart code area for mobile contact transfer"></div>

    <div class="contact">
      <h2 class="person">Brent Ashdown</h2>
      <p class="title">Chartered Accountant</p>
      <ul class="contact-list">
        <li>+61 (0) 437 215604
          <svg viewBox="0 0 16 16" aria-hidden="true"><path d="M4 1h3l1 4-2 1.5a9 9 0 0 0 3.5 3.5L11 8l4 1v3c0 1-1 2-2 2A12 12 0 0 1 2 3c0-1 1-2 2-2z" fill="#fff"/></svg>
        </li>
        <li>brent@rowfinsvc-example.com.au
          <svg viewBox="0 0 16 16" aria-hidden="true"><rect x="1" y="3" width="14" height="10" fill="none" stroke="#fff" stroke-width="1.4"/><path d="M1 3l7 6 7-6" fill="none" stroke="#fff" stroke-width="1.4"/></svg>
        </li>
        <li>brent7312
          <svg viewBox="0 0 16 16" aria-hidden="true"><circle cx="8" cy="8" r="7" fill="#fff"/></svg>
        </li>
        <li>ABN 71 309 482 157
          <svg viewBox="0 0 16 16" aria-hidden="true"><rect x="2" y="2" width="12" height="12" fill="none" stroke="#fff" stroke-width="1.4"/></svg>
        </li>
        <li>17 Wattlebank Street Norvale SA 5174
          <svg viewBox="0 0 16 16" aria-hidden="true"><path d="M8 15s5-5.5 5-9A5 5 0 0 0 3 6c0 3.5 5 9 5 9z" fill="#fff"/><circle cx="8" cy="6" r="2" fill="#231f20"/></svg>
        </li>
      </ul>
    </div>
  </section>

</main>
</body>
</html>
```